HPTW Morvane Terrace Bathroom Remodeling Postcard

We are a bathroom remodeling contractor in Los Angeles, California called Harbor Peak Tile Works. We want to create a postcard to send out to a specific condominium complex in the city of Burbank called Morvane Terrace. The postcard will be advertising a specific offer and should showcase our professionalism and quality of work. We have experience working in this particular housing development so we want to communicate that we are familiar with it. We want to be the first contractor that comes to mind when anyone who lives here starts thinking about a bathroom remodel in their home.

The postcard design should be an eye-catching combination of text and photos. The attached photos can be cropped if necessary. We have sent a variety of photos to choose from. Not all of the photos need to be included.

This is the specific text that should appear on the postcard:

Attn: Morvane Terrace Homeowners

2015 Bathroom Remodeling Sales Event!

Now through June 1, 2015 | Call Today for Details

Complete Custom Remodels Starting at $9999 (Labor and Materials)

14 days, Start to Finish, Fully-Permitted

Professional, Courteous, Quick & Clean!

harborpeaktileworks.example

Licensed (#452016), Bonded and Insured

818-555-0147

Morvane Terrace customer references available upon request. Some restrictions apply. Ad price for bathroom with tub/shower combo, call for price on shower only bathroom. Hard costs for permits not included. Tax on finish materials not included. Call today to lock in your special savings.

```html
<!DOCTYPE html>
<html lang="en">
<head>
<meta charset="utf-8">
<title>HPTW Morvane Terrace Bathroom Remodeling Postcard</title>
<link rel="stylesheet" href="https://fonts.googleapis.com/css2?family=Roboto+Condensed:ital,wght@0,400;0,700;1,700&family=Source+Sans+3:wght@400;600&display=swap">
<style>
  :root {
    --backdrop: #d9dbde;
    --navy: #0f4a77;
    --navy-deep: #0b3c63;
    --teal: #22b3b6;
    --teal-light: #3fc9c4;
    --white: #ffffff;
    --ink-blue: #1a5fa8;
    --line-grey: #9a9a9a;
    --tile-a: #2aa7c9;
    --tile-b: #6cc24a;
    --tile-c: #5a4fa8;
  }
  * { box-sizing: border-box; margin: 0; padding: 0; }
  html, body { width: 1200px; height: 1153px; overflow: hidden; }
  body { background: var(--backdrop); position: relative; font-family: "Source Sans 3", sans-serif; }

  .postcard { position: absolute; left: 100px; width: 1000px; height: 520px; box-shadow: 0 6px 18px rgba(0,0,0,.25); overflow: hidden; }

  /* ---------- Back ---------- */
  .postcard-back { top: 40px; background: var(--white); color: var(--ink-blue); }
  .back-brand { position: absolute; left: 60px; top: 40px; width: 300px; text-align: center; }
  .brand-mark { display: flex; align-items: center; justify-content: center; gap: 10px; }
  .brand-square { width: 26px; height: 26px; background: var(--ink-blue); }
  .brand-initials { font-family: "Roboto Condensed", sans-serif; font-weight: 700; font-size: 40px; letter-spacing: 2px; }
  .brand-name { font-family: "Roboto Condensed", sans-serif; font-size: 23px; line-height: 1.1; margin-top: 10px; text-transform: uppercase; }
  .fine-print { position: absolute; left: 40px; top: 185px; width: 340px; font-size: 15.5px; line-height: 1.32; color: var(--ink-blue); padding: 0 26px 0 30px; }
  .quote-mark { position: absolute; font-family: Georgia, serif; font-size: 52px; color: #9aa6b2; line-height: 1; }
  .quote-open { left: 0; top: -6px; }
  .quote-close { right: 0; bottom: -30px; }
  .contact-list { position: absolute; left: 60px; top: 370px; list-style: none; font-size: 16px; }
  .contact-list li { display: flex; align-items: center; gap: 10px; margin-bottom: 16px; }
  .contact-list svg { width: 20px; height: 20px; fill: var(--ink-blue); }
  .stamp-box { position: absolute; right: 60px; top: 30px; width: 84px; height: 104px; border: 1.5px solid #555; }
  .address-line { position: absolute; left: 560px; width: 380px; border-top: 1.5px dotted var(--line-grey); }

  /* ---------- Front ---------- */
  .postcard-front { top: 593px; background: var(--navy); color: var(--white); font-family: "Roboto Condensed", sans-serif; }
  .front-brand { position: absolute; left: 28px; top: 48px; display: flex; align-items: center; gap: 8px; }
  .front-brand .brand-square { background: var(--white); width: 20px; height: 20px; }
  .front-brand .brand-initials { font-size: 30px; color: var(--white); }
  .headline { position: absolute; left: 170px; top: 14px; font-style: italic; font-weight: 700; line-height: 1.05; }
  .headline-attn { color: var(--teal-light); font-size: 42px; }
  .headline-event { color: var(--white); font-size: 34px; }
  .photo-frame { position: absolute; left: 210px; top: 118px; width: 540px; height: 300px; background: var(--teal); padding: 8px; display: flex; gap: 8px; }
  .photo { flex: 1; }
  .photo-glass { background: linear-gradient(160deg, #d8dcd8, #a7aea8 60%, #8a6f55); }
  .photo-tile { background: linear-gradient(160deg, #b47d5c, #7d4a33 55%, #5a3a2a); }
  .tile-pattern { position: absolute; background: linear-gradient(135deg, var(--tile-a), var(--tile-b) 45%, var(--tile-c)); opacity: .9; }
  .pattern-left { left: 22px; top: 170px; width: 170px; height: 120px; }
  .pattern-right { left: 775px; top: 70px; width: 200px; height: 140px; }
  .offer { position: absolute; left: 22px; top: 305px; width: 180px; text-align: center; font-size: 21px; line-height: 1.1; }
  .offer-price { display: flex; align-items: center; justify-content: center; gap: 6px; margin-top: 2px; }
  .offer-price strong { font-size: 38px; font-weight: 700; }
  .offer-price small { font-size: 12px; line-height: 1.05; text-align: left; }
  .deadline { position: absolute; left: 770px; top: 225px; width: 210px; text-align: center; font-size: 21px; line-height: 1.15; }
  .deadline-phone { font-size: 34px; font-weight: 700; margin-top: 4px; }
  .ribbon { position: absolute; background: var(--teal); color: var(--white); font-weight: 700; font-style: italic; display: flex; align-items: center; justify-content: center; clip-path: polygon(4% 0, 100% 0, 96% 50%, 100% 100%, 0 100%, 4% 50%, 0 0); }
  .ribbon-days { left: 420px; top: 430px; width: 560px; height: 40px; font-size: 23px; text-transform: uppercase; }
  .ribbon-service { left: 0; top: 448px; width: 420px; height: 40px; font-size: 22px; clip-path: polygon(0 0, 100% 0, 96% 50%, 100% 100%, 0 100%); }
  .web-address { position: absolute; left: 640px; top: 478px; font-size: 15px; font-weight: 700; }
  .license { position: absolute; left: 110px; top: 492px; font-size: 14px; font-weight: 700; }
</style>
</head>
<body>

<section class="postcard postcard-back" aria-label="Postcard back">
  <div class="back-brand">
    <div class="brand-mark"><span class="brand-square"></span><span class="brand-initials">HPTW</span></div>
    <p class="brand-name">Harbor Peak<br>Tile Works</p>
  </div>
  <p class="fine-print">
    <span class="quote-mark quote-open">&ldquo;</span>
    Morvane Terrace customer references available upon request. Some restrictions apply. Ad price for bathroom with tub/shower combo, call for price on shower only bathroom. Hard costs for permits not included. Tax on finish materials not included. Call today to lock in your special savings.
    <span class="quote-mark quote-close">&rdquo;</span>
  </p>
  <ul class="contact-list">
    <li><svg viewBox="0 0 20 20"><path d="M10 2 1 10h3v8h5v-5h2v5h5v-8h3z"/></svg>7720 Alderbank Blvd #310 Tarzana, California 91300</li>
    <li><svg viewBox="0 0 20 20"><path d="M5 2l3 4-2 2c1 2 3 4 5 5l2-2 4 3-2 3C9 17 3 11 2 5z"/></svg>818-555-0147</li>
    <li><svg viewBox="0 0 20 20"><circle cx="10" cy="10" r="8" fill="none" stroke="#1a5fa8" stroke-width="2"/><path d="M2 10h16M10 2c-4 5-4 11 0 16M10 2c4 5 4 11 0 16" fill="none" stroke="#1a5fa8" stroke-width="1.5"/></svg>harborpeaktileworks.example</li>
  </ul>
  <div class="stamp-box"></div>
  <div class="address-line" style="top:190px"></div>
  <div class="address-line" style="top:260px"></div>
  <div class="address-line" style="top:330px"></div>
</section>

<section class="postcard postcard-front" aria-label="Postcard front">
  <div class="front-brand"><span class="brand-square"></span><span class="brand-initials">HPTW</span></div>
  <h1 class="headline">
    <span class="headline-attn">Attn: Morvane Terrace Homeowners</span><br>
    <span class="headline-event">2015 Bathroom Remodeling Sales Event!</span>
  </h1>
  <div class="tile-pattern pattern-left" role="img" aria-label="Decorative cube mosaic pattern in blue, green and purple"></div>
  <div class="tile-pattern pattern-right" role="img" aria-label="Decorative cube mosaic pattern in blue, green and purple"></div>
  <div class="photo-frame">
    <div class="photo photo-glass" role="img" aria-label="Photo of remodeled glass shower with light stone tile"></div>
    <div class="photo photo-tile" role="img" aria-label="Photo of remodeled walk-in shower with brown tile and rain head"></div>
  </div>
  <div class="offer">
    Complete Custom<br>Remodels Starting at
    <div class="offer-price"><strong>$9999</strong><small>Labor<br>and Materials</small></div>
  </div>
  <div class="deadline">
    Now through June 1, 2015<br>Call Today for Details
    <div class="deadline-phone">818-555-0147</div>
  </div>
  <div class="ribbon ribbon-days">14 Days, Start to Finish, Fully-Permitted</div>
  <p class="web-address">www.harborpeaktileworks.example</p>
  <div class="ribbon ribbon-service">Professional, Courteous, Quick &amp; Clean!</div>
  <p class="license">Licensed (#452016), Bonded and Insured</p>
</section>

</body>
</html>
```